Need a cover for eBook:
Title is: 41 Blunders That Sink Your Indie-Released Volume.
Remarks about the title: I know that is difficult to design a cover with a number. You can add the word TOP (in caps or not) before 41 blunders. It is not mandatory to insert the word TOP. It is up to you if you think you can create a better cover.
Subtitle is: A Newcomer's Manual for Releasing Solo, Arranging Pictures and Words, Planning Pages, Boosting Sign-ups and Moving More Copies
Author: Dennis R. Walbrey
Publisher: Quillmark Press
The book made the presentation of errors that can occur during the production of an ebook. Title must be big, the title should be readable even when the image is reduced in size. No photo please.
I join my projects as an example. Do what you want but I need impact.

Target Market(s)

Book to sell first at Brimfold Reader Shop. Target is authors, men or women, who want to produce ebooks.

Industry/Entity Type

Publishing Company

Font styles to use
Sans Serif

Colors
3176b5
9bcb3c

Requirements
Must have
• High readability when cover is small.
• Here is the definition of the word KILL
• put an end to or cause the failure or defeat of (something).
• "the committee voted to kill the project"
• synonyms: destroy, put an end to, end, extinguish, dash, quash, ruin, wreck, shatter, smash, crush, scotch, thwart; informalput the kibosh on, stymie, scuttle
• "this would kill all hopes of progress"
• veto, defeat, vote down, rule against, reject, throw out, overrule, overturn, put a stop to, quash, squash
• "an opposition attempt to kill the bill"
Nice to have
• I suggested 2 colors but you can you use another one or two. I want cover that sell. There is so bright ideas here. Come on down!
Should not have
• No picture or photo. If a photo or an object had power to the cover, you can insert one. I don't want a photo-collage.

```html
<!DOCTYPE html>
<html lang="en">
<head>
<meta charset="utf-8">
<title>41 Blunders That Sink Your Indie-Released Volume — Cover</title>
<link rel="stylesheet" href="https://fonts.googleapis.com/css2?family=Fredoka:wght@500;600;700&family=Nunito:wght@800&family=Oswald:wght@600&display=swap">
<style>
  :root {
    --stage: #d6d6d6;
    --green: #9bcb3c;
    --blue: #3176b5;
    --white: #ffffff;
    --pencil-wood: #e3d3a2;
  }
  * { box-sizing: border-box; margin: 0; padding: 0; }
  html, body {
    width: 1200px;
    height: 1200px;
    overflow: hidden;
    background: var(--stage);
  }
  .cover {
    position: absolute;
    left: 217px;
    top: 60px;
    width: 765px;
    height: 1080px;
    background: var(--green);
    overflow: hidden;
  }
  .cover__lower-band {
    position: absolute;
    left: 0;
    top: 793px;
    width: 100%;
    height: 287px;
    background: var(--blue);
  }
  .cover__author {
    position: absolute;
    top: 58px;
    width: 100%;
    text-align: center;
    font-family: "Nunito", sans-serif;
    font-weight: 800;
    font-size: 44px;
    line-height: 1.2;
    color: var(--white);
  }
  .cover__art,
  .title {
    position: absolute;
    left: 0;
    top: 0;
    width: 765px;
    height: 1080px;
  }
  .title__number {
    font-family: "Fredoka", sans-serif;
    font-weight: 700;
    font-size: 370px;
    fill: var(--blue);
    stroke: var(--white);
    stroke-width: 8px;
    paint-order: stroke fill;
  }
  .title__word,
  .title__line {
    font-family: "Oswald", sans-serif;
    font-weight: 600;
    fill: var(--white);
    stroke: var(--blue);
    stroke-width: 3px;
    paint-order: stroke fill;
  }
  .title__word { font-size: 135px; }
  .title__line { font-size: 115px; }
  .title__tagline {
    font-family: "Fredoka", sans-serif;
    font-weight: 600;
    font-size: 56px;
    fill: var(--blue);
  }
  .cover__subtitle {
    position: absolute;
    left: 50px;
    top: 866px;
    width: 665px;
    text-align: center;
    font-family: "Fredoka", sans-serif;
    font-weight: 500;
    font-size: 25px;
    line-height: 1.32;
    color: var(--white);
  }
  .cover__publisher {
    position: absolute;
    top: 996px;
    width: 100%;
    text-align: center;
    font-family: "Fredoka", sans-serif;
    font-weight: 600;
    font-size: 28px;
    line-height: 1.2;
    color: var(--white);
  }
</style>
</head>
<body>
  <main class="cover">
    <div class="cover__lower-band"></div>

    <svg class="cover__art" viewBox="0 0 765 1080" role="img" aria-label="Illustration of two striped pencils, one lying across the cover and one standing upright on the right, breaking through the blue band">
      <rect x="0" y="738" width="700" height="86" fill="var(--pencil-wood)"/>
      <rect x="679" y="180" width="82" height="640" fill="var(--pencil-wood)"/>
    </svg>

    <p class="cover__author">Dennis R. Walbrey</p>

    <svg class="title" viewBox="0 0 765 1080" role="heading" aria-level="1" aria-label="41 Blunders That Sink Your Indie-Released Volume">
      <text class="title__number" x="82" y="502" textLength="340" lengthAdjust="spacingAndGlyphs">41</text>
      <text class="title__word" x="433" y="363" textLength="221" lengthAdjust="spacingAndGlyphs">BLUN</text>
      <text class="title__word" x="433" y="483" textLength="221" lengthAdjust="spacingAndGlyphs">DERS</text>
      <text class="title__line" x="90" y="603" textLength="564" lengthAdjust="spacingAndGlyphs">THAT SINK YOUR</text>
      <text class="title__tagline" x="124" y="672" textLength="533" lengthAdjust="spacingAndGlyphs">INDIE-RELEASED VOLUME</text>
    </svg>

    <p class="cover__subtitle">A Newcomer's Manual for Releasing Solo, Arranging Pictures and Words, Planning Pages, Boosting Sign-ups and Moving More Copies</p>

    <p class="cover__publisher">Quillmark Press</p>
  </main>
</body>
</html>
```